Optometric Practice needs Initial Photoshop Mockup

We need a graphic design for the homepage of a website for an optometric practice that specializes in vision therapy.

Here's the link to the project folder on Filecove. I've included photos, example sites, content and instructions.

https://www.filecove.net/sh/qk7tmd3wz8rb2n5/BBX_HrLpVaQyJk6mTcDRZeNu

Please feel free to submit any questions about the design. I'll be happy to help guide you in any areas you're uncertain of.

Okay - I've updated the project to payment confirmed. Let's see some designs :) Thanks, Wes

```html
<!DOCTYPE html>
<html lang="en">
<head>
<meta charset="utf-8">
<title>Clearpath Vision Learning Centers</title>
<link href="https://fonts.googleapis.com/css2?family=Open+Sans:wght@400;600;700&display=swap" rel="stylesheet">
<style>
:root{
  --red:#8e0a0a;
  --red-dark:#6f0606;
  --navy:#24248c;
  --navy-btn:#2d2d9e;
  --ink:#222;
  --muted:#777;
  --panel:#eeeef0;
  --side:#f1f1f3;
  --footer:#f4f4f4;
  --bar:#2b2b2b;
  --hero:#f2e5de;
}
*{box-sizing:border-box;margin:0;padding:0}
html,body{width:1200px;height:2192px;overflow:hidden;background:#fff}
body{font-family:"Open Sans",Arial,sans-serif;color:var(--ink);position:relative}
.abs{position:absolute}
a{color:var(--navy);text-decoration:none}

/* header */
.brand{left:100px;top:26px;display:flex;align-items:center;gap:12px}
.brand-dot{width:26px;height:26px;border-radius:50%;background:var(--red)}
.brand-name{font-size:34px;font-weight:700;color:var(--red);letter-spacing:.5px}
.contact{right:380px;top:44px;text-align:right;white-space:nowrap}
.contact .doc{font-size:15px;color:#444;line-height:20px}
.contact .phone{font-size:23px;color:var(--red);font-weight:600;line-height:28px}
.phone-icon{left:830px;top:56px}
.appt{left:884px;top:50px;width:216px;height:41px;background:var(--navy-btn);color:#fff;font-size:16px;display:flex;align-items:center;justify-content:center;border-radius:2px}

/* nav */
.nav{left:0;top:146px;width:1200px;height:55px;background:var(--red)}
.nav ul{list-style:none;display:flex;position:absolute;left:100px;top:0;height:55px}
.nav li{color:#fff;font-size:14.5px;padding:0 12.5px;line-height:55px;white-space:nowrap}
.nav li.active{background:#2a2a2a}

/* hero */
.hero{left:0;top:201px;width:1200px;height:483px;background:var(--hero)}
.hero-photo{left:486px;top:201px;width:614px;height:483px;background:linear-gradient(90deg,#f3e4dc 0%,#e9d5ca 40%,#c9a995 60%,#e4d2c6 100%)}
.hero-title{left:100px;top:310px;font-size:28.5px;color:var(--navy);font-weight:400;white-space:nowrap}
.hero-text{left:101px;top:356px;width:420px;font-size:13.5px;line-height:21px;color:#666}
.hero-btn{left:101px;top:442px;width:155px;height:40px;background:#2b2b2b;color:#fff;font-size:15.5px;display:flex;align-items:center;justify-content:center;border-radius:2px}
.dots{left:102px;top:510px;width:80px;height:20px;background:#666;border-radius:10px;display:flex;gap:8px;align-items:center;justify-content:center}
.dots span{width:8px;height:8px;border-radius:50%;background:#fff}
.dots span.on{background:#666;border:2px solid #fff}

/* main */
.welcome{left:99px;top:722px;font-size:26.5px;color:var(--navy);font-weight:600;white-space:nowrap}
.intro{left:101px;top:772px;width:716px;font-size:14px;line-height:22px;color:#666}
.bio{left:101px;top:903px;width:720px;height:274px;background:var(--panel)}
.bio-photo{left:580px;top:903px;width:241px;height:274px;background:linear-gradient(135deg,#f6f6f8,#e9dfd7 55%,#f1ede9)}
.bio-text{left:127px;top:945px;width:370px;font-size:15px;line-height:27px;color:#777}
.provide{left:101px;top:1222px;font-size:17px;color:#222}
.services{left:101px;top:1262px;width:700px;list-style:none}
.services li{position:relative;padding-left:22px;font-size:14.5px;line-height:22.5px;color:#777;margin-bottom:17px}
.services li::before{content:"";position:absolute;left:2px;top:10px;width:3px;height:3px;background:#777;border-radius:50%}
.services b{font-weight:400;color:#222}

/* sidebar */
.side{left:840px;top:684px;width:260px;height:1128px;background:var(--side)}
.side-h{left:852px;top:723px;font-size:21px;color:var(--navy);font-weight:600}
.video{left:852px;top:763px;width:238px;height:150px;background:linear-gradient(120deg,#2b1a1a,#5c3a34 45%,#1d2238)}
.play{left:952px;top:819px;width:38px;height:38px;border-radius:50%;background:rgba(0,0,0,.55)}
.card-blue{left:852px;top:931px;width:238px;height:92px;background:var(--navy);color:#fff;font-size:17.5px;font-weight:600;text-align:center;display:flex;align-items:center;justify-content:center;line-height:25px}
.card-photo{left:852px;top:1023px;width:238px;height:152px;background:linear-gradient(120deg,#6f8f4a,#d8b49a 45%,#a77e5e 75%,#8fa860)}
.badge{left:869px;top:1196px;width:200px;height:49px;border-radius:6px;background:linear-gradient(#f4f4f4,#cfcfcf);border:1px solid #aaa}
.social-box{left:852px;top:1267px;width:238px;height:219px;background:#fff;border:1px solid #cfd4dd}
.social-box .top{font-size:9px;font-weight:700;color:#333;background:#eef0f5;padding:3px 5px;border-bottom:1px solid #cfd4dd}
.sb-avatar{left:7px;top:23px;width:34px;height:34px;background:#c9b8a8}
.sb-name{left:48px;top:23px;font-size:10.5px;color:var(--navy);font-weight:700;line-height:13px;width:180px}
.sb-like{left:48px;top:52px;width:38px;height:14px;background:#3c5a98;color:#fff;font-size:8px;text-align:center;line-height:14px}
.sb-count{left:6px;top:80px;font-size:8.5px;color:#555;line-height:11px;width:225px;border-top:1px solid #ddd;padding-top:5px}
.sb-grid{left:6px;top:118px;display:grid;grid-template-columns:repeat(5,37px);gap:5px 8px}
.sb-grid span{height:37px;background:#c9c2bb}
.sb-grid span:nth-child(2n){background:#8f8a86}
.sb-grid span:nth-child(3n){background:#d7a56a}
.card-success{left:852px;top:1504px;width:238px;height:83px;background:var(--navy);color:#fff;font-size:17.5px;text-align:center;display:flex;align-items:center;justify-content:center;line-height:25px}
.quote{left:852px;top:1587px;width:238px;height:161px;background:#fff;text-align:center}
.quote p{position:absolute;left:38px;top:26px;width:162px;font-size:13.5px;line-height:21px;color:#777;font-style:italic}
.quote .who{position:absolute;left:0;width:238px;top:124px;font-size:14px;color:#222}
.qmark{font-size:44px;color:#d6d6d6;font-family:Georgia,serif;position:absolute;line-height:1}

/* footer */
.footer{left:0;top:1812px;width:1200px;height:300px;background:var(--footer)}
.f-brand{left:108px;top:1858px;display:flex;align-items:center;gap:10px}
.f-brand .brand-dot{width:18px;height:18px}
.f-brand .brand-name{font-size:24px}
.office{font-size:14.5px;line-height:25px;color:#555}
.office strong{display:block;font-size:16px;color:#222;font-weight:600;line-height:24px}
.f-divider{left:791px;top:1848px;width:1px;height:235px;background:#ccc}
.browse-h{left:816px;top:1846px;font-size:19px;color:#222}
.links{list-style:none;font-size:13.5px;color:#777;line-height:27px}
.links li::before{content:"• "}
.f-badge{left:813px;top:2034px;width:154px;height:38px;border-radius:5px;background:linear-gradient(#f6f6f6,#d3d3d3);border:1px solid #aaa}
.bar{left:0;top:2112px;width:1200px;height:80px;background:var(--bar)}
.copy{left:101px;top:2142px;font-size:13px;color:#ccc}
.socials{left:855px;top:2134px;display:flex;gap:9px}
.socials span{width:33px;height:33px;border-radius:50%}
</style>
</head>
<body>

<header>
  <div class="abs brand"><span class="brand-dot"></span><span class="brand-name">Clearpath</span></div>
  <div class="abs contact">
    <div class="doc">Dr. Daniel Ferrow</div>
    <div class="phone">410-555-0142</div>
  </div>
  <svg class="abs phone-icon" width="30" height="28" viewBox="0 0 30 28"><path d="M4 4c4-3 8-3 12 0 4 3 6 7 8 10l2 4-4 3-3-5c-2-3-4-5-7-6-3-1-5 0-6 1z" fill="var(--red)"/></svg>
  <div class="abs appt">Request an Appointment</div>
</header>

<nav class="abs nav">
  <ul>
    <li class="active">Meet Us</li><li>New Patients</li><li>Vision &amp; Learning</li><li>Vision Therapy</li><li>Binocular Vision Disorders</li><li>Head Injuries</li><li>Professionals</li><li>Contact Us</li>
  </ul>
</nav>

<section>
  <div class="abs hero"></div>
  <div class="abs hero-photo" role="img" aria-label="Photo of two young girls standing back to back"></div>
  <h1 class="abs hero-title">Improving Vision, Changing Lives</h1>
  <p class="abs hero-text">Aenean nec scelerisque est. Class aptent taciti sociosqu ad litora torquent per conubia nostra, per inceptos himenaeos. Ut ultricies felis et orci cursus feugiat.</p>
  <div class="abs hero-btn">Get Started Now</div>
  <div class="abs dots"><span class="on"></span><span></span><span></span><span></span></div>
</section>

<main>
  <h2 class="abs welcome">WELCOME TO CLEARPATH VISION LEARNING CENTERS</h2>
  <p class="abs intro">There are many visual skills critical for reading and learning. Often, a vision problem is misdiagnosed as an attention problem or a learning disability due to similarity of symptoms. Anyone who is struggling with reading, has poor reading comprehension, or just isn't performing to their full potential, should consider scheduling a developmental vision evaluation. To help determine if you or your child should be tested, <a>Do the Checklist</a> on our <a>Vision Quiz page</a>.</p>
  <div class="abs bio"></div>
  <div class="abs bio-photo" role="img" aria-label="Photo of a smiling girl reading a book"></div>
  <p class="abs bio-text"><a>Dr. Daniel Ferrow</a> is a developmental optometrist who specializes in the diagnosis and treatment of vision problems that interfere with reading and learning. He is a member of the National Optometric Society, the College of Vision Development Practitioners, and a Fellow in the Academy of Clinical Optometry.</p>
  <h3 class="abs provide" style="font-weight:400">Clearpath Vision Learning Centers and Dr. Daniel Ferrow provide :</h3>
  <ul class="abs services">
    <li>Comprehensive <b>Eye Examinations</b> for All Ages, including Infants and Preschoolers</li>
    <li><b>Vision Therapy</b> for All Ages</li>
    <li>Treatment for <b>Learning-related Vision Problems</b></li>
    <li>Free Monthly Seminars. Visit our Linkbook page for information about our free monthly seminars on a variety of topics, including: <b>The Hidden Disability - Undiagnosed Vision Problems.</b></li>
    <li>Continuing Education seminars for Optometrists, Occupational Therapists and Physical Therapists. All CE offerings are free and board approved. For CE information and dates, see our <b>success stories, blogs and videos on Binocular Vision Disorders</b></li>
    <li>Treatment for <b>Binocular Vision Conditions,</b> such as <b>Amblyopia or Lazy Eye, Convergence Insufficiency</b> (near vision disorder), <b>Diplopia</b> (double vision), <b>Lack of Stereopsis</b> (two-eyed depth perception), and <b>Strabismus</b> (cross-eyed, wandering eye, eye turns, etc.)</li>
    <li><b>Visual Rehabilitation for Patients with Special Needs, such as Developmental Delays or Traumatic Brain Injury (TBI)</b>, including Autism, Stroke, Whiplash, CP, MS, etc.</li>
    <li>Treatment for <b>Stress-related Visual Problems</b>, including Blurred Vision, Visual Stress from Reading and Computers, Eye Strain Headaches, and/or Vision-induced Stomachaches or Motion Sickness</li>
    <li><b>Sports Vision</b> Correction and/or Improvement</li>
  </ul>
</main>

<aside>
  <div class="abs side"></div>
  <h2 class="abs side-h">FEATURED VIDEO</h2>
  <div class="abs video" role="img" aria-label="Video still of a news presenter"></div>
  <svg class="abs play" viewBox="0 0 38 38"><path d="M15 11l12 8-12 8z" fill="#fff"/></svg>
  <div class="abs card-blue">DOES MY CHILD HAVE<br>A VISION PROBLEM?</div>
  <div class="abs card-photo" role="img" aria-label="Photo of a mother hugging her daughter"></div>
  <div class="abs badge" role="img" aria-label="Reviews badge"></div>
  <div class="abs social-box">
    <div class="top">Find us online</div>
    <div class="abs sb-avatar"></div>
    <div class="abs sb-name">Clearpath: Dr. Daniel Ferrow, Developmental Optometrist</div>
    <div class="abs sb-like">Like</div>
    <div class="abs sb-count">155 people like Clearpath: Dr. Daniel Ferrow, Developmental Optometrist.</div>
    <div class="abs sb-grid" role="img" aria-label="Grid of follower photos"><span></span><span></span><span></span><span></span><span></span><span></span><span></span><span></span><span></span><span></span></div>
  </div>
  <div class="abs card-success">SUCCESS WITH<br>VISION THERAPY</div>
  <div class="abs quote">
    <span class="qmark" style="left:22px;top:14px">“</span>
    <p>Pellentesque non nisi molestie, vestibulum tellus at, congue velit. laoreet nisl bibendum.</p>
    <span class="qmark" style="left:164px;top:96px">”</span>
    <div class="who">Anna Reyes</div>
  </div>
</aside>

<footer>
  <div class="abs footer"></div>
  <div class="abs f-brand"><span class="brand-dot"></span><span class="brand-name">Clearpath</span></div>
  <div class="abs office" style="left:108px;top:1920px"><strong>Clearpath Vision Learning Centers</strong><strong>Dr. Daniel Ferrow</strong>4120 Larkspur Pkwy.<br>Meridian Plaza, Ste. 3, Easton, MD, 21601<br>Phone: 410-555-0142<br>Fax: 410-555-0187</div>
  <div class="abs office" style="left:465px;top:1920px"><strong>Clearpath Vision Learning Centers</strong><strong>Dr. Daniel Ferrow</strong>56 Harrow Ave. Suite 200, Room 3<br>Glenwood, MD, 21738<br>Phone: 410-555-0142</div>
  <div class="abs f-divider"></div>
  <h3 class="abs browse-h" style="font-weight:400">Browse Our Site</h3>
  <ul class="abs links" style="left:816px;top:1882px"><li>Home</li><li>Meet Us</li><li>New Patients</li><li>Vision &amp; Learning</li><li>Vision Therapy</li></ul>
  <ul class="abs links" style="left:984px;top:1882px;width:116px;line-height:17px"><li style="margin:5px 0 11px">Binocular Vision Disorders</li><li style="margin-bottom:10px">Head Injuries</li><li style="margin-bottom:10px">Professionals</li><li>Contact Us</li></ul>
  <div class="abs f-badge" role="img" aria-label="Reviews badge"></div>
  <div class="abs bar"></div>
  <div class="abs copy">Copyright © 2014 &nbsp;Clearpath Vision Learning Centers , Inc. &nbsp; All rights reserved</div>
  <div class="abs socials"><span style="background:#3b5b99"></span><span style="background:#2aa3de"></span><span style="background:#555"></span><span style="background:#f06a1d"></span><span style="background:#d9302a"></span><span style="background:#5aa848"></span></div>
</footer>

</body>
</html>
```